Exciting opportunity to create logo and a label for our natural health brand.

About us

We are a customer centric health supplement brand who believes in natural medicine and high quality ingredients. We take a holistic approach to healthcare, with an eastern philosophy. We believe in being partners with our customers in their health care journey and are invested in their well being.

Our brand philosophy and values are attached (see Varo philosophy.png). Our personality traits are:

- Natural
- Fresh
- Modern
- Balanced (in a holistic sense)

Task breakdown

1. Design a fresh feeling logo for us
- We want it to represent our values and high quality ingredients. We would like the quality of the product to be reflected in the branding and have a high end feel.
- Logo text must include Varo Health Sciences
- We want the Varo to be the focus of the logo (see uploaded image Varo logo example.png)
The logo does not have to follow this layout, but we just want the Varo to stand out. Feel free to use your creative license on this!

2. Create an attractive label to go on the supplement bottle
- The designs need to be eye catching, give a sense of high end ingredients and natural products and tie in with the logo to give a joined up feel.
- We are selling our products online and need them to really stand out from the competition.
- See examples of labels and packaging we like (1 -7 label design).

The initial label we would like you to design would be for our product Calm Haven. It is a product that assists in the management of Anxiety and stress. The label will appear on the bottle that holds the capsules for this supplement, see uploaded files (Example plain bottles.png). The bottles may be white as the picture shows or dark blue recyclable plastic or dark brown glass . We don't have the exact dimensions of the bottle yet, but I will follow up with these.

The label needs to include the following things:
1. The logo
2. The name of the product
3. The product is to help with the relief of Anxiety and Stress
4. Number of capsules the bottle contains
5. The back of the label should have
i) The ingredients
ii) Dosage
iii) Directions of use

Please use placeholder text where needed.

We look forward to seeing your design. Thank you.

```html
<!DOCTYPE html>
<html lang="en">
<head>
<meta charset="utf-8">
<title>Varo Health Sciences – Calm Haven Label</title>
<link href="https://fonts.googleapis.com/css2?family=Open+Sans:wght@400;600;700;800&family=Michroma&family=Open+Sans+Condensed:wght@700&display=swap" rel="stylesheet">
<style>
  :root{
    --paper:#f7f7f4;
    --green:#7cb342;
    --green-light:#a5d06a;
    --ink:#222;
    --grey:#6b6b6b;
    --title:#5e5e5e;
    --white:#fff;
  }
  *{box-sizing:border-box;margin:0;padding:0}
  html,body{width:1200px;height:756px;overflow:hidden}
  body{background:linear-gradient(#ececec,#bdbdbd);font-family:"Open Sans",Arial,sans-serif;color:var(--ink)}
  .label{position:absolute;left:40px;top:198px;width:1120px;height:360px;display:flex;background:var(--paper);box-shadow:0 6px 20px rgba(0,0,0,.18)}
  .panel{position:relative;width:373.33px;height:100%;overflow:hidden}
  .panel svg.shape{position:absolute;inset:0}

  /* back panel */
  .barcode-zone{position:absolute;left:-8px;top:150px;transform:rotate(90deg);font-size:12px;color:var(--grey);letter-spacing:.3px}
  .directions{position:absolute;left:70px;top:34px;width:270px;font-size:8.6px;line-height:1.35;text-align:justify}
  .directions p{margin-bottom:10px}
  .directions .free-from{font-size:7.4px}
  .back-band{position:absolute;left:0;right:0;top:258px;height:84px;background:var(--green)}
  .fda-note{position:absolute;left:26px;top:24px;width:226px;background:var(--white);border-radius:6px;padding:6px 8px;font-size:6.6px;line-height:1.3}

  /* front panel */
  .brand{position:absolute;left:38px;top:34px}
  .brand-name{display:flex;align-items:center;gap:6px;font-weight:800;font-size:54px;line-height:1;color:var(--green);letter-spacing:-1px}
  .brand-dot{width:12px;height:12px;border-radius:50%;background:var(--green)}
  .brand-sub{font-size:13px;color:var(--grey);letter-spacing:1px;margin-top:2px}
  .product{position:absolute;left:38px;top:140px;font-family:"Michroma",sans-serif;font-weight:400;font-size:15px;line-height:1.1;color:var(--title)}
  .product .dose{font-size:10px;color:var(--green);margin-left:6px}
  .product .purpose{display:block;font-size:10.5px;margin-top:3px}
  .tagline{position:absolute;left:34px;top:197px;font-family:"Michroma",sans-serif;font-size:10.5px;color:var(--green)}
  .count{position:absolute;left:20px;top:274px;width:135px;text-align:right;color:var(--white);font-family:"Open Sans Condensed",sans-serif;font-weight:700;font-size:14px;line-height:1}
  .count small{display:block;font-size:9px;margin-top:3px;font-family:"Open Sans",sans-serif;font-weight:700}
  .divider{position:absolute;left:162px;top:240px;width:2px;height:98px;background:var(--white)}
  .promise{position:absolute;left:172px;top:254px;width:180px;color:var(--white);font-family:"Open Sans Condensed",sans-serif;font-weight:700;font-size:11px;line-height:1.25}

  /* facts panel */
  .facts{position:absolute;left:118px;top:20px;width:220px;height:232px;background:var(--white);border-radius:12px;padding:8px 10px;font-size:6.4px;line-height:1.35}
  .facts h2{text-align:center;font-size:15px;font-weight:800;margin-bottom:3px}
  .facts table{width:100%;border-collapse:collapse;margin-top:3px}
  .facts th{font-size:6.4px;text-align:right;border-top:4px solid var(--ink);border-bottom:1px solid var(--ink);padding:1px 0}
  .facts td{border-bottom:1px solid #999;padding:1px 0}
  .facts td.amt{text-align:right;padding-right:14px}
  .facts td.dv{text-align:right;width:24px}
  .facts .indent{padding-left:6px}
  .facts .notes{border-top:3px solid var(--ink);margin-top:4px;padding-top:2px;font-weight:700}
  .facts .other{margin-top:6px}
  .maker{position:absolute;left:122px;top:276px;color:var(--white);font-size:9px;font-weight:600}
  .address{position:absolute;left:118px;top:292px;width:84px;height:36px;background:var(--white);border-radius:10px;display:flex;align-items:center;justify-content:center;font-size:7px}
</style>
</head>
<body>
<main class="label">

  <section class="panel panel-back">
    <span class="barcode-zone">Bar-Code Zone</span>
    <div class="directions">
      <p>Suggested Use: For adults, take two (2) capsules daily, preferably with a meal or as directed by your doctor.</p>
      <p>Caution: If you are pregnant, nursing, taking any medications, planning any medical procedure or have any medical condition, consult your doctor before use. Discontinue use and consult your doctor if any adverse reactions occur.</p>
      <p>May cause drowsiness. Do not drive or operate machinery if affected.</p>
      <p>KEEP OUT OF REACH OF CHILDREN. DO NOT USE IF SAFETY SEAL IS DAMAGED OR MISSING. STORE IN A COOL DRY PLACE.</p>
      <p class="free-from">No Artificial Color, Flavor or Sweetener, No Preservatives, No Sugar, No Starch, No Milk, No Lactose, No Gluten, No Wheat, No Yeast, No Sodium.</p>
    </div>
    <div class="back-band">
      <p class="fda-note">†These statements have not been evaluated by the FDA. This product is not intended to diagnose, cure, treat or prevent any disease.</p>
    </div>
  </section>

  <section class="panel panel-front">
    <svg class="shape" width="374" height="360" viewBox="0 0 374 360" aria-hidden="true">
      <path d="M0 0 H374 V58 C300 58 230 30 150 4 L140 0 Z" fill="var(--green)"/>
      <path d="M0 24 C90 10 160 6 220 0 H150 C90 8 40 16 0 20 Z" fill="var(--green-light)"/>
      <path d="M0 248 C70 244 130 236 170 222 C230 205 300 212 374 210 V330 C300 330 240 338 170 346 C110 350 50 344 0 342 Z" fill="var(--green)"/>
    </svg>
    <div class="brand">
      <div class="brand-name">Varo<span class="brand-dot"></span></div>
      <div class="brand-sub">Health Sciences</div>
    </div>
    <h1 class="product">CALM HAVEN<span class="dose">500mg</span><span class="purpose">ANXIETY &amp; STRESS RELIEF</span></h1>
    <p class="tagline">Natural - Fresh - Modern - Balanced</p>
    <p class="count">60 CAPSULES<small>DIETARY SUPPLEMENT</small></p>
    <span class="divider"></span>
    <p class="promise">NATURAL MEDICINE AND HIGH QUALITY INGREDIENTS</p>
  </section>

  <section class="panel panel-facts">
    <svg class="shape" width="374" height="360" viewBox="0 0 374 360" aria-hidden="true">
      <path d="M0 0 H374 V40 C250 40 120 26 0 20 Z" fill="var(--green)"/>
      <path d="M0 230 C120 224 250 214 374 212 V330 C250 332 120 340 0 344 Z" fill="var(--green)"/>
    </svg>
    <div class="facts">
      <h2>Supplement Facts</h2>
      <div>Serving Size: 2 Capsules<br>Servings Per Container: 30</div>
      <table>
        <tr><th>Amount Per Serving</th><th></th><th>% DV</th></tr>
        <tr><td>Vitamin B6</td><td class="amt">2 mg</td><td class="dv">118%</td></tr>
        <tr><td>Magnesium (as glycinate)</td><td class="amt">100 mg</td><td class="dv">24%</td></tr>
        <tr><td>Calm Haven Blend</td><td class="amt">500 mg</td><td class="dv">**</td></tr>
        <tr><td class="indent">Ashwagandha Root Extract</td><td class="amt">200 mg</td><td class="dv">**</td></tr>
        <tr><td class="indent">L-Theanine</td><td class="amt">150 mg</td><td class="dv">**</td></tr>
        <tr><td class="indent">Lemon Balm Leaf Extract</td><td class="amt">100 mg</td><td class="dv">**</td></tr>
        <tr><td class="indent">Chamomile Flower Extract</td><td class="amt">50 mg</td><td class="dv">**</td></tr>
      </table>
      <p class="notes">** (%DV) Daily Value not established<br>* Percent Daily Values are based on a 2,000 calorie diet.</p>
      <p class="other">Other Ingredients: Vegetable Cellulose Capsule, Rice Flour, Magnesium Stearate.</p>
    </div>
    <p class="maker">Manufactured for:</p>
    <div class="address">Adress</div>
  </section>

</main>
</body>
</html>
```